professional business card design

Business card design. Photos have been uploaded and i am open to the designer choosing which photos to use. Would like the card to be mostyly in a grey scale design with black, whites, silver & grey colours. I have added copy of our flyer as would like on the back side of card our services to be listed. Do not use any bright colurs such as blue red green or yellow. i need to be able to edit the phone number and naem in the final card design submitted.

Target Market(s)

Clients

Industry/Entity Type

earhmovibng and transport

Contact Information for Business Card

Director Name, address, email, phone number and services

Colors

Designer to choose only greyscale colors for use in the design.

Requirements
Should not have
• no yellow, red, blue or green

```html
<!DOCTYPE html>
<html lang="en">
<head>
<meta charset="utf-8">
<title>Haulcrest Pty Ltd – Business Card</title>
<link href="https://fonts.googleapis.com/css2?family=Rajdhani:wght@500;600;700&display=swap" rel="stylesheet">
<style>
  :root{
    --page:#232927;
    --card:#000000;
    --white:#ffffff;
    --silver:#c8c8c8;
    --grey:#9a9a9a;
    --ink:#1a1a1a;
    --band:linear-gradient(90deg,#ffffff 0%,#d9d9d9 30%,#9c9c9c 55%,#e6e6e6 80%,#ffffff 100%);
    --rule:linear-gradient(90deg,#f2f2f2 0%,#a8a8a8 25%,#5e5e5e 50%,#bdbdbd 75%,#f4f4f4 100%);
  }
  *{box-sizing:border-box;margin:0;padding:0}
  html,body{width:1200px;height:1200px;overflow:hidden}
  body{background:var(--page);font-family:"Rajdhani",sans-serif;color:var(--white);position:relative}
  .card{position:absolute;left:170px;width:860px;height:499px;background:var(--card);overflow:hidden}
  .card--front{top:55px}
  .card--back{top:646px}

  .wordmark{position:absolute;font-weight:700;color:var(--silver);letter-spacing:2px;white-space:nowrap;transform:translateX(-50%)}
  .wordmark small{font-size:.42em;letter-spacing:0;margin-left:10px}
  .card--front .wordmark{left:430px;top:48px;font-size:92px;line-height:1}
  .card--back .wordmark{left:430px;top:22px;font-size:54px;line-height:1}

  .front-rule{position:absolute;left:0;right:0;top:207px;height:3px;background:var(--white)}
  .identity{position:absolute;top:280px;left:0;width:408px;text-align:right}
  .identity .name{font-size:46px;font-weight:600;line-height:1}
  .identity .title{font-size:32px;font-weight:500;color:var(--grey);line-height:1;margin-top:2px}
  .divider{position:absolute;left:422px;top:284px;width:2px;height:70px;background:var(--white)}
  .contact{position:absolute;left:446px;top:284px;font-size:25px;font-weight:500;line-height:33px}
  .contact li{list-style:none;display:flex;align-items:center;gap:14px}
  .contact svg{width:22px;height:22px;flex:none}
  .address-band{position:absolute;left:0;right:0;top:431px;height:38px;background:var(--band);color:var(--ink);
    display:flex;align-items:center;justify-content:center;gap:8px;font-size:23px;font-weight:600}
  .address-band svg{width:20px;height:22px}

  .back-band{position:absolute;left:0;right:0;top:128px;height:21px;background:var(--rule)}
  .services-title{position:absolute;left:54px;top:175px;font-size:32px;font-weight:600;letter-spacing:.5px}
  .services{position:absolute;top:232px;list-style:none;font-size:23px;font-weight:600;line-height:32.6px}
  .services li{position:relative;padding-left:26px}
  .services li::before{content:"";position:absolute;left:0;top:12px;width:10px;height:10px;border-radius:50%;background:var(--white)}
  .services li.cont::before{display:none}
  .services--left{left:54px}
  .services--right{left:540px}
  .back-rule{position:absolute;left:0;right:0;top:465px;height:3px;background:var(--white)}
</style>
</head>
<body>

<section class="card card--front" aria-label="Business card front">
  <div class="wordmark">HAULCREST<small>Pty Ltd</small></div>
  <div class="front-rule"></div>
  <div class="identity">
    <div class="name">YOUR NAME</div>
    <div class="title">Director</div>
  </div>
  <div class="divider"></div>
  <ul class="contact">
    <li>
      <svg viewBox="0 0 24 24" aria-hidden="true"><rect x="6" y="2" width="12" height="20" rx="2" fill="none" stroke="#fff" stroke-width="2"/><circle cx="12" cy="18" r="1.3" fill="#fff"/></svg>
      +00 000 0000
    </li>
    <li>
      <svg viewBox="0 0 24 24" aria-hidden="true"><rect x="2" y="5" width="20" height="14" fill="#fff"/><path d="M2 5l10 8 10-8M2 19l8-7M22 19l-8-7" fill="none" stroke="#000" stroke-width="1.6"/></svg>
      yourmail@haulcrest.com
    </li>
  </ul>
  <div class="address-band">
    <svg viewBox="0 0 20 22" aria-hidden="true"><path d="M10 2a6 6 0 0 0-6 6c0 4.5 6 10 6 10s6-5.5 6-10a6 6 0 0 0-6-6z" fill="none" stroke="#1a1a1a" stroke-width="2"/><circle cx="10" cy="8" r="2.2" fill="#1a1a1a"/><path d="M4 20h12" stroke="#1a1a1a" stroke-width="2"/></svg>
    Depot: Lot 14, Ironbark Track Red Plains
  </div>
</section>

<section class="card card--back" aria-label="Business card back">
  <div class="wordmark">HAULCREST<small>Pty Ltd</small></div>
  <div class="back-band"></div>
  <h2 class="services-title">OUR SERVICES :</h2>
  <ul class="services services--left">
    <li>Over Size Loads / Hot Shot Loads</li>
    <li>Heavy Vehicle Recovery Services</li>
    <li>Potable Water Deliveris</li>
    <li>Road Building / Maintenance</li>
    <li>Earthworks</li>
    <li>Sand &amp; Metal&nbsp; Supply &amp; Carage</li>
  </ul>
  <ul class="services services--right">
    <li>Road Train Tippers</li>
    <li>Road Train Tankers</li>
    <li>Road Train Flat Tops</li>
    <li>Drop Deck Trailers</li>
    <li>Mine Site Accredited</li>
    <li class="cont">Equipment &amp; Operators</li>
  </ul>
  <div class="back-rule"></div>
</section>

</body>
</html>
```